Business Card For Nightclub Industry

We're looking for a business card for our company GlintPulse. We're interested in finishing options including die-cut, foil, 2 opposing rounded corners (not 4 rounded corners) and spot UV.

The card should be elegant yet refined to reflect a high tech company.

The front of the cart should be bold with the glintpulse logo across. IF you choose to use a foil option, apply it to the glintpulse logo.

The back of the card will list our other company and product logos along with their related text and links.

Target Market(s)

video professionals
club owners
event promoters
nightclubs
DJs

Industry/Entity Type

Business

Contact Information for Business Card

Dario Fenwick
Founder & CEO

GlintPulse LLC <-- this line is optional as it is implied from the main logo
742 W. Calder Row
Austin, TX 78519
888.412.3096 x517

Font styles to use
Sans Serif

Requirements
Must have
• Front side logo:
• GlintPulse (logo attached)
• Premium Visuals For Live Events
• www.glintpulse-example.com
• --------
• Back side of card logos (equal sizing):
• GlintMarks (use glintpulse logo as placeholder; we are working on that logo now)
• Custom 3D Logo Animations
• www.glintmarks-example.com
• GlintBeams (use glintpulse logo as placeholder; we are working on that logo now)
• Professional Laser Systems
• www.glintbeams-example.com
• Quavix (logo)
• Visual Software & Media Servers
• www.quavix-example.net
• ReelCanvasHQ (logo)
• Premixed DVDs & BluRay
• www.discprisma-example.com
• Additional logos to add:
• ZephyrClips (logo)
• Cascade Fetchmaster (logo)
• Halberd Optics (logo)
• Clipnok (logo)
Nice to have
• Spot UV
• Foil
• Opposing Rounded Corners
• Matches the feel of our new website (attached pic)
• You are not required to implement the exact logo colors as they appear in the attachments. For instance, if you want to replace all the logos with chrome this might be a good option.

```html
<!DOCTYPE html>
<html lang="en">
<head>
<meta charset="utf-8">
<title>GlintPulse Business Card</title>
<link rel="stylesheet" href="https://fonts.googleapis.com/css2?family=Lato:wght@300;400;700&display=swap">
<style>
  :root {
    --backdrop: #3a3a3a;
    --card: #050a14;
    --gold: #f7b500;
    --white: #ffffff;
    --muted: #b9bcc2;
    --rule: #d9d9d9;
  }
  * { margin: 0; padding: 0; box-sizing: border-box; }
  html, body { width: 1200px; height: 900px; overflow: hidden; }
  body {
    background: var(--backdrop);
    font-family: "Lato", Arial, sans-serif;
    position: relative;
  }
  .card {
    position: absolute;
    top: 193px;
    width: 297px;
    height: 513px;
    background: var(--card);
  }
  .card--front { left: 288px; border-radius: 34px 0 34px 0; text-align: center; }
  .card--back { left: 616px; border-radius: 0 34px 0 34px; }

  .front-mark {
    position: absolute; left: 0; right: 0; top: 196px;
    display: flex; flex-direction: column; align-items: center; gap: 14px;
  }
  .front-mark__dot {
    width: 70px; height: 70px; border-radius: 50%;
    background: var(--gold);
  }
  .front-mark__name {
    font-size: 27px; font-weight: 400; color: var(--white); letter-spacing: 0.3px;
  }
  .tagline {
    position: absolute; left: 0; right: 0; top: 357px;
    font-size: 13px; line-height: 17px; color: var(--muted);
  }
  .front-url {
    position: absolute; left: 0; right: 0; top: 442px;
    font-size: 12.5px; color: var(--white);
  }
  .front-url .accent { color: var(--gold); }

  .back-mark {
    position: absolute; left: 40px; top: 34px;
    display: flex; align-items: center; gap: 8px;
  }
  .back-mark__dot { width: 20px; height: 20px; border-radius: 50%; background: var(--gold); }
  .back-mark__name { font-size: 25px; color: var(--white); }

  .contact {
    position: absolute; left: 79px; top: 80px;
    font-size: 11.5px; line-height: 14.5px; color: var(--white);
  }
  .contact__name { font-size: 13.5px; font-weight: 700; color: var(--gold); }
  .contact__lines { margin-top: 14px; }

  .divider {
    position: absolute; left: 79px; top: 180px;
    width: 176px; height: 1px; background: var(--rule);
  }

  .brand {
    position: absolute; left: 79px;
    font-size: 11px; line-height: 14px;
  }
  .brand__name { font-size: 17px; line-height: 20px; color: var(--white); margin-bottom: 1px; }
  .brand__desc { font-weight: 300; color: var(--muted); }
  .brand__url { font-weight: 700; color: var(--gold); }
  .brand--marks { top: 203px; }
  .brand--beams { top: 260px; }
  .brand--reel { top: 319px; }
  .brand--quavix { top: 388px; }
  .brand--quavix .brand__name { font-size: 22px; line-height: 26px; }

  .partners {
    position: absolute; left: 36px; right: 30px; top: 474px;
    display: flex; justify-content: space-between; align-items: center;
    font-size: 9px; font-weight: 700; color: var(--muted);
  }
  .partners .gold { color: var(--gold); }
</style>
</head>
<body>
  <section class="card card--front">
    <div class="front-mark">
      <span class="front-mark__dot"></span>
      <span class="front-mark__name">glintpulse</span>
    </div>
    <p class="tagline">Premium Visuals<br>For Live Events</p>
    <p class="front-url">www.<span class="accent">glintpulse</span>-example.com</p>
  </section>

  <section class="card card--back">
    <div class="back-mark">
      <span class="back-mark__dot"></span>
      <span class="back-mark__name">glintpulse</span>
    </div>

    <div class="contact">
      <p class="contact__name">Dario Fenwick</p>
      <p>Founder &amp; CEO</p>
      <p class="contact__lines">888.412.3096 x517<br>742 W. Calder Row<br>Austin, TX 78519</p>
    </div>

    <div class="divider"></div>

    <div class="brand brand--marks">
      <p class="brand__name">glintmarks</p>
      <p class="brand__desc">Custom 3D Logo Animations</p>
      <p class="brand__url">www.glintmarks-example.com</p>
    </div>
    <div class="brand brand--beams">
      <p class="brand__name">glintbeams</p>
      <p class="brand__desc">Professional Laser Systems</p>
      <p class="brand__url">www.glintbeams-example.com</p>
    </div>
    <div class="brand brand--reel">
      <p class="brand__name">ReelCanvasHQ</p>
      <p class="brand__desc">Premixed DVDs &amp; BluRay</p>
      <p class="brand__url">www.discprisma-example.com</p>
    </div>
    <div class="brand brand--quavix">
      <p class="brand__name">quavix</p>
      <p class="brand__desc">Visual Software &amp; Media Servers</p>
      <p class="brand__url">www.quavix-example.net</p>
    </div>

    <div class="partners">
      <span class="gold">ZephyrClips</span>
      <span class="gold">Cascade Fetchmaster</span>
      <span>Halberd Optics</span>
      <span class="gold">Clipnok</span>
    </div>
  </section>
</body>
</html>
```